Australian residential property business needs a business card design

I need a business card design for my new business 'Meadow Estate Partners'. The business will involve house purchases, land development sites, renovation projects, sub-divisions etc. I will be buying property from motivated vendors and working with property investors. I will deal with a wide range of people working in the residential property market including real estate agents, councils, tradespeople, banks, home owners, etc.

I would like something simple, not flashy, but a little bit unique. The colours should be in line with my logo. The business card needs to be professional. I would like something memorable, but not 'busy' or too bright. Not boring. Modern ok.

Target Market(s)

Home owners looking to sell their property, real estate agents, tradespeople (e.g. plumbers, builders, electricians etc), property investors, local councils, and anyone else involved in the residential property industry

Industry/Entity Type

Business

Contact Information for Business Card

I need to include my business name/logo, my name, my title, a PO Box number/address, a mobile number, and an email address.

Font styles to use
Serif

Requirements
Must have
• My business card details listed above.

```html
<!DOCTYPE html>
<html lang="en">
<head>
<meta charset="UTF-8">
<title>Meadow Estate Partners — Business Card</title>
<link rel="stylesheet" href="https://fonts.googleapis.com/css2?family=Arimo:wght@400;700&display=swap">
<style>
  :root {
    --stage: #2b2824;
    --card-black: #0b0b0b;
    --card-sheen: #2a2a2a;
    --band-white: #f2f2f2;
    --band-shadow: #d4d4d4;
    --accent-gold: #e8d21e;
    --brand-gold: #e9b42a;
    --text-light: #e6e6e6;
    --text-grey: #5a5a5a;
  }
  * { box-sizing: border-box; margin: 0; padding: 0; }
  html, body {
    width: 1200px;
    height: 1023px;
    overflow: hidden;
    background: var(--stage);
    font-family: "Arimo", Arial, sans-serif;
  }
  .stage {
    width: 1200px;
    height: 1023px;
    display: flex;
    align-items: center;
    justify-content: center;
  }
  .card {
    position: relative;
    width: 840px;
    height: 480px;
    border-radius: 6px;
    overflow: hidden;
    background:
      linear-gradient(115deg, transparent 38%, rgba(255,255,255,0.08) 48%, rgba(255,255,255,0.03) 60%, transparent 70%),
      linear-gradient(160deg, var(--card-sheen) 0%, var(--card-black) 55%);
    box-shadow: 0 20px 50px rgba(0,0,0,0.55);
  }
  .brand {
    position: absolute;
    left: 64px;
    top: 150px;
    display: flex;
    align-items: center;
    gap: 14px;
  }
  .brand-square {
    width: 34px;
    height: 34px;
    background: var(--brand-gold);
  }
  .brand-name {
    color: var(--brand-gold);
    font-weight: 700;
    font-size: 30px;
    letter-spacing: 0.5px;
    text-transform: uppercase;
  }
  .person {
    position: absolute;
    right: 56px;
    top: 258px;
    text-align: right;
    padding-right: 14px;
    border-right: 3px solid var(--accent-gold);
  }
  .person-name {
    color: var(--accent-gold);
    font-weight: 700;
    font-size: 27px;
    letter-spacing: 0.5px;
    text-transform: uppercase;
  }
  .person-title {
    color: var(--text-light);
    font-size: 17px;
    margin-top: 6px;
  }
  .info-band {
    position: absolute;
    left: 0;
    right: 0;
    bottom: 0;
    height: 118px;
    background: linear-gradient(180deg, #ffffff 0%, var(--band-white) 60%, var(--band-shadow) 100%);
    display: flex;
    justify-content: space-between;
    align-items: center;
    padding: 0 56px 0 64px;
    color: var(--text-grey);
    font-size: 18px;
    line-height: 1.55;
  }
  .contact-list {
    list-style: none;
    text-align: right;
  }
  .contact-list li {
    display: flex;
    align-items: center;
    justify-content: flex-end;
    gap: 12px;
  }
  .contact-icon {
    width: 16px;
    height: 16px;
    fill: var(--text-grey);
  }
</style>
</head>
<body>
  <main class="stage">
    <article class="card">
      <div class="brand">
        <span class="brand-square"></span>
        <span class="brand-name">Meadow Estate Partners</span>
      </div>

      <div class="person">
        <p class="person-name">Avery Lane</p>
        <p class="person-title">General manager</p>
      </div>

      <footer class="info-band">
        <address class="postal" style="font-style: normal;">
          14 Wattle Grove<br>
          Bendale, VIC 3999
        </address>
        <ul class="contact-list">
          <li>
            <span>0000-987-654</span>
            <svg class="contact-icon" viewBox="0 0 24 24" aria-hidden="true">
              <path d="M6.6 10.8a15.1 15.1 0 0 0 6.6 6.6l2.2-2.2a1 1 0 0 1 1-.25 11.4 11.4 0 0 0 3.6.57 1 1 0 0 1 1 1V20a1 1 0 0 1-1 1A17 17 0 0 1 3 4a1 1 0 0 1 1-1h3.5a1 1 0 0 1 1 1c0 1.25.2 2.45.57 3.57a1 1 0 0 1-.25 1z"/>
            </svg>
          </li>
          <li>
            <span>hello@meadowestate.example</span>
            <svg class="contact-icon" viewBox="0 0 24 24" aria-hidden="true">
              <path d="M3 5h18a1 1 0 0 1 1 1v12a1 1 0 0 1-1 1H3a1 1 0 0 1-1-1V6a1 1 0 0 1 1-1zm1 2.2V17h16V7.2l-8 5.3z M4.6 7 12 11.9 19.4 7z"/>
            </svg>
          </li>
        </ul>
      </footer>
    </article>
  </main>
</body>
</html>
```